Quarvex Power Point Template - Institutional Presentation

Develop a comprehensive template for a corporate presentation power point.

The presentation will be aimed to institutional investors.

Style to be modern and contemporary. Use of icons and images welcome but not to much.

It would be great if you could develop the layout/style for the content in the following slides:

- Cover
- Section title
- Slide with title and bullet points on one side and two text boxes on the other side
- Slide with line chart and pie chart
- Slide with table

Should we like the slides above we will then develop the rest of the template.

We may then need to have a dark-background version - but this will be invoiced separately.

Target Market(s)

Corporate institutional investors

Industry/Entity Type

Finance

Font styles to use
Serif
Sans Serif

Colors
3176b5
0255a3
cee9f5
86cae7
33a6d7
0792cd
33b8a4
00a990
86cfc6

Requirements
Must have
• Mostly white background with minimal objects
Nice to have
• Use of photos, but not to much.

```html
<!DOCTYPE html>
<html lang="en">
<head>
<meta charset="utf-8">
<title>Quarvex Presentation Template</title>
<link href="https://fonts.googleapis.com/css2?family=Raleway:wght@400;500;600;700;800&family=Open+Sans:wght@400;600&display=swap" rel="stylesheet">
<style>
:root{
  --navy:#1d2a4e;
  --navy-2:#243560;
  --teal:#33b8a4;
  --teal-light:#86cfc6;
  --blue:#0792cd;
  --blue-2:#33a6d7;
  --sky:#cee9f5;
  --grey:#9aa0ad;
  --bar-grey:#8e929b;
  --line:#dfe3ea;
  --canvas:#eef0f4;
  --white:#ffffff;
}
*{box-sizing:border-box;margin:0;padding:0}
html,body{width:990px;height:1200px;overflow:hidden;background:var(--canvas)}
body{font-family:"Open Sans",sans-serif;color:var(--navy)}
.deck{position:relative;width:990px;height:1200px;display:grid;grid-template-columns:repeat(3,325px);grid-template-rows:repeat(6,183px);column-gap:5px;row-gap:16px;padding:7px 4px}
.slide{position:relative;background:var(--white);overflow:hidden;box-shadow:0 1px 4px rgba(20,30,60,.18)}
.title{position:absolute;left:14px;top:14px;font-family:"Raleway",sans-serif;font-weight:700;font-size:14px;letter-spacing:-.1px;color:var(--navy);white-space:nowrap}
.title::after{content:"";position:absolute;left:0;bottom:-3px;width:28px;height:1.5px;background:var(--navy)}
.badge{position:absolute;right:12px;top:13px;width:60px;height:14px;background:var(--navy);color:var(--white);font-family:"Raleway",sans-serif;font-weight:700;font-size:7px;letter-spacing:1.2px;display:flex;align-items:center;justify-content:center}
.footer{position:absolute;left:0;right:0;bottom:0;height:8px;background:var(--navy);color:#c7cbd6;font-size:3.4px;display:flex;align-items:center;justify-content:space-between;padding:0 4px}
.tiny{font-size:4.2px;line-height:1.4;color:var(--grey)}
.tiny b{color:var(--navy);font-weight:600}
.abs{position:absolute}
.center{text-align:center}
.bullets{position:absolute;list-style:none}
.bullets li{position:relative;padding-left:6px;margin-bottom:5px;font-size:4.2px;line-height:1.4;color:var(--grey)}
.bullets li::before{content:"";position:absolute;left:0;top:1.6px;width:2px;height:2px;border-radius:50%;background:var(--navy)}
.bullets li.spacer{height:5px;margin:0;padding:0}
.bullets li.spacer::before{display:none}
.bullets li b{color:var(--navy);font-weight:600}
.text-box{position:absolute;padding:7px 8px}
.text-box h4{font-family:"Raleway",sans-serif;font-weight:600;font-size:6.5px;margin-bottom:3px}
.box-dark{background:var(--navy);color:var(--white)}
.box-dark p{color:#c9cfdc}
.box-line{border:1.2px solid var(--navy)}
.box-line h4{color:var(--navy)}
.data-table{position:absolute;left:24px;top:64px;width:280px;border-collapse:collapse;font-size:4px}
.data-table th{background:var(--navy);color:var(--white);font-weight:600;height:9px}
.data-table td{height:10.3px;text-align:center;color:var(--grey);border-bottom:.5px solid var(--line)}
.data-table td:first-child,.data-table th:first-child{text-align:left;padding-left:8px}
.data-table tr:nth-child(even) td{background:#f4f5f8}
.band-head{position:absolute;left:0;right:0;top:0;height:30px;background:var(--navy);display:flex;align-items:center;justify-content:space-between;padding:0 14px 0 16px;color:var(--white);font-family:"Raleway",sans-serif}
.band-head h2{font-size:14px;font-weight:700}
.band-head span{font-size:7px;font-weight:700;letter-spacing:1.2px}
.price-band{position:absolute;left:0;right:0;top:92px;height:48px;background:var(--navy)}
.plan{position:absolute;background:var(--white);box-shadow:0 1px 3px rgba(0,0,0,.15);text-align:center}
.plan-head{color:var(--white);font-family:"Raleway",sans-serif;font-size:12px;font-weight:500;padding-top:5px;height:27px;line-height:1}
.plan-head small{display:block;font-size:3.5px;margin-top:1px}
.plan ul{list-style:none;font-size:3.5px;color:var(--grey)}
.plan li{padding:4px 0;border-bottom:.5px solid var(--line);margin:0 8px}
.plan li:last-child{border:none}
.photo{position:absolute}
.divider-text{position:absolute;left:8px;top:113px;color:var(--white);font-family:"Raleway",sans-serif}
.divider-text small{display:block;font-size:5px;text-align:center;width:150px}
.divider-text h2{font-size:15px;font-weight:700}
.divider-text p{font-size:7px;color:#c9cfdc;text-align:center;width:150px}
.brand-light{position:absolute;right:14px;top:16px;color:var(--white);font-family:"Raleway",sans-serif;font-weight:800;font-size:13px;letter-spacing:1.5px}
.icon{position:absolute;border-radius:50%;display:flex;align-items:center;justify-content:center}
.icon svg{width:55%;height:55%}
.feat{position:absolute;font-size:4.2px;line-height:1.4;color:var(--grey)}
.feat b{display:block;color:var(--navy);font-weight:600;font-size:5px}
.col-box{position:absolute;top:86px;width:59px;height:80px;color:var(--white);text-align:center;font-size:3.6px;line-height:1.4;padding-top:32px}
.col-box .icon{left:19px;top:10px;width:20px;height:20px;background:var(--white)}
.col-box b{display:block;font-weight:600;margin-bottom:2px}
.col-item{position:absolute;top:62px;width:60px;text-align:center}
.col-item .ring{width:38px;height:38px;border-radius:50%;margin:0 auto;display:flex;align-items:center;justify-content:center;border:4px solid}
.col-item h5{font-family:"Raleway",sans-serif;font-size:5px;font-weight:700;margin:5px 0 3px;color:var(--navy)}
.kp{position:absolute;top:77px;width:43px;height:43px;border-radius:50%;color:var(--white);display:flex;flex-direction:column;align-items:center;justify-content:center;font-size:4px;line-height:1.25;text-align:center}
.kp svg{width:9px;height:9px;margin-bottom:1px}
.year{position:absolute;width:36px;height:36px;border-radius:50%;color:var(--white);text-align:center;font-family:"Raleway",sans-serif;font-size:8px;padding-top:10px;line-height:1}
.year small{display:block;font-size:2.6px;margin-top:1px;line-height:1.2}
.member{position:absolute;width:140px}
.avatar{position:absolute;width:34px;height:34px;border-radius:50%}
.member-info{position:absolute;left:40px;top:4px;width:110px}
.member-info h5{font-size:5.3px;font-weight:600}
.member-info p{font-size:3.6px;line-height:1.35;color:var(--navy)}
.member-info ul{list-style:disc;padding-left:5px;font-size:3.3px;color:var(--grey);line-height:1.35;margin-top:1px}
.legend{position:absolute;display:flex;gap:6px;font-size:3.2px;color:var(--grey)}
.legend i{display:inline-block;width:3px;height:3px;margin-right:1.5px;vertical-align:middle}
.contact-panel{position:absolute;left:0;top:0;width:146px;bottom:0;background:var(--navy-2);color:var(--white);padding:26px 0 0 43px;font-family:"Raleway",sans-serif}
.contact-panel .brand{font-weight:800;font-size:13px;letter-spacing:1.5px}
.contact-panel h3{font-size:14px;font-weight:700;margin:23px 0 12px -1px;position:relative}
.contact-panel h3::after{content:"";position:absolute;left:0;bottom:-3px;width:28px;height:1.5px;background:var(--white)}
.contact-line{display:flex;gap:6px;font-family:"Open Sans",sans-serif;font-size:5px;line-height:1.3;margin-bottom:6px;margin-left:-1px}
.contact-line svg{width:6px;height:6px;flex:none;margin-top:.5px}
.socials{display:flex;gap:5px;margin:10px 0 0 30px}
.socials span{width:8px;height:8px;border-radius:50%;background:var(--white)}
.thanks{position:absolute;left:146px;right:0;top:105px;text-align:center;color:var(--white);font-family:"Raleway",sans-serif}
.thanks h2{font-size:15px;font-weight:700;letter-spacing:.3px}
.thanks p{font-size:6px}
.thanks small{display:block;font-size:4.8px;margin-top:5px;line-height:1.3}
</style>
</head>
<body>
<main class="deck">

<section class="slide">
  <h2 class="title">Your Table Area</h2><div class="badge">QUARVEX</div>
  <p class="abs tiny" style="left:24px;top:42px;width:190px;font-size:3.6px"><b>Description</b> Short note on the purpose of the table and the key figures it reports for the period under review.</p>
  <table class="data-table">
    <tr><th>Item</th><th>Value</th><th>Value</th><th>Value</th><th>Value</th></tr>
    <tr><td>Lorem ipsum</td><td>10</td><td>15</td><td>16</td><td>18</td></tr>
    <tr><td>Lorem ipsum</td><td>12</td><td>13</td><td>15</td><td>16</td></tr>
    <tr><td>Lorem ipsum</td><td>20</td><td>22</td><td>21</td><td>21</td></tr>
    <tr><td>Lorem ipsum</td><td>10</td><td>21</td><td>12</td><td>11</td></tr>
    <tr><td>Lorem ipsum</td><td>25</td><td>25</td><td>25</td><td>25</td></tr>
    <tr><td>Lorem ipsum</td><td>10</td><td>02</td><td>51</td><td>21</td></tr>
    <tr><td>Lorem ipsum</td><td>35</td><td>36</td><td>85</td><td>32</td></tr>
    <tr><td>Lorem ipsum</td><td>26</td><td>33</td><td>35</td><td>32</td></tr>
    <tr><td>Lorem ipsum</td><td>32</td><td>10</td><td>32</td><td>32</td></tr>
  </table>
  <div class="footer"><span>© 2017 QUARVEX. All rights reserved</span><span>37</span></div>
</section>

<section class="slide">
  <div class="band-head"><h2>Your Blank Slide</h2><span>QUARVEX</span></div>
  <div class="footer"><span>© 2017 QUARVEX. All rights reserved</span><span>38</span></div>
</section>

<section class="slide">
  <h2 class="title">Bullet Points And Two Text Boxes</h2><div class="badge">QUARVEX</div>
  <ul class="bullets" style="left:14px;top:44px;width:150px">
    <li><b>Lorem ipsum dolor sit amet</b> consectetur adipiscing elit, sed do eiusmod tempor incididunt ut labore magna.</li>
    <li><b>Ut enim ad minim veniam</b> quis nostrud exercitation ullamco laboris nisi ut aliquip commodo.</li>
    <li><b>Duis aute irure dolor</b> in reprehenderit in voluptate velit esse cillum dolore fugiat nulla.</li>
    <li class="spacer"></li>
    <li><b>Lorem ipsum dolor sit amet</b> consectetur adipiscing elit, sed do eiusmod tempor incididunt ut labore magna.</li>
    <li><b>Ut enim ad minim veniam</b> quis nostrud exercitation ullamco laboris nisi ut aliquip commodo.</li>
    <li><b>Duis aute irure dolor</b> in reprehenderit in voluptate velit esse cillum dolore fugiat nulla.</li>
  </ul>
  <div class="text-box box-dark tiny" style="left:206px;top:38px;width:108px;height:62px"><h4>Heading Goes Here</h4><p>Lorem ipsum dolor sit amet, consectetur adipiscing elit, sed do eiusmod tempor incididunt ut labore magna aliqua.</p><p style="margin-top:3px">Duis aute irure dolor in reprehenderit in voluptate velit esse dolore.</p></div>
  <div class="text-box box-dark tiny" style="left:206px;top:106px;width:108px;height:62px"><h4>Heading Goes Here</h4><p>Lorem ipsum dolor sit amet, consectetur adipiscing elit, sed do eiusmod tempor incididunt ut labore magna aliqua.</p><p style="margin-top:3px">Duis aute irure dolor in reprehenderit in voluptate velit esse dolore.</p></div>
  <div class="footer"><span>© 2017 QUARVEX. All rights reserved</span><span>39</span></div>
</section>

<section class="slide">
  <h2 class="title">Bullet Points And Two Text Boxes</h2><div class="badge">QUARVEX</div>
  <div class="text-box box-line tiny" style="left:14px;top:38px;width:148px;height:62px"><h4>Heading Goes Here</h4><p>Lorem ipsum dolor sit amet, consectetur adipiscing elit, sed do eiusmod tempor incididunt ut labore magna aliqua.</p><p style="margin-top:3px">Duis aute irure dolor in reprehenderit in voluptate velit esse dolore.</p></div>
  <div class="text-box box-line tiny" style="left:14px;top:106px;width:148px;height:62px"><h4>Heading Goes Here</h4><p>Lorem ipsum dolor sit amet, consectetur adipiscing elit, sed do eiusmod tempor incididunt ut labore magna aliqua.</p><p style="margin-top:3px">Duis aute irure dolor in reprehenderit in voluptate velit esse dolore.</p></div>
  <ul class="bullets" style="left:172px;top:38px;width:140px">
    <li><b>Lorem ipsum dolor sit amet</b> consectetur adipiscing elit, sed do eiusmod tempor incididunt ut labore.</li>
    <li><b>Ut enim ad minim veniam</b> quis nostrud exercitation ullamco laboris nisi ut aliquip.</li>
    <li><b>Duis aute irure dolor</b> in reprehenderit in voluptate velit esse cillum dolore fugiat.</li>
    <li class="spacer"></li>
    <li><b>Lorem ipsum dolor sit amet</b> consectetur adipiscing elit, sed do eiusmod tempor incididunt ut labore.</li>
    <li><b>Ut enim ad minim veniam</b> quis nostrud exercitation ullamco laboris nisi ut aliquip.</li>
    <li><b>Duis aute irure dolor</b> in reprehenderit in voluptate velit esse cillum dolore fugiat.</li>
  </ul>
  <div class="footer"><span>© 2017 QUARVEX. All rights reserved</span><span>40</span></div>
</section>

<section class="slide">
  <h2 class="title" style="left:24px">Monthly Subscription</h2><div class="badge">QUARVEX</div>
  <div class="price-band"></div>
  <div class="plan" style="left:47px;top:61px;width:80px;height:91px"><div class="plan-head" style="background:var(--teal)">$300<small>per month</small></div><ul><li>Single Edition</li><li>50gb Cloud Service</li><li>3 User</li><li>Free Update</li></ul></div>
  <div class="plan" style="left:122px;top:55px;width:81px;height:105px;z-index:1"><div class="plan-head" style="background:var(--navy);height:34px;padding-top:9px">$900<small>per month</small></div><ul><li>Business Edition</li><li>80gb Cloud Service</li><li>8 User</li><li>Free Update</li></ul></div>
  <div class="plan" style="left:199px;top:61px;width:80px;height:91px"><div class="plan-head" style="background:var(--blue)">$400<small>per month</small></div><ul><li>Single Edition</li><li>30gb Cloud Service</li><li>3 User</li><li>Free Update</li></ul></div>
</section>

<section class="slide" style="background:var(--navy)">
  <div class="photo" role="img" aria-label="Tinted photo of tall office buildings seen from below" style="inset:0;background:linear-gradient(135deg,#34446e 0%,#243560 45%,#1d2a4e 100%)"></div>
  <div class="brand-light">QUARVEX</div>
  <div class="divider-text"><small>Divider Page</small><h2>Your Title Goes Here</h2><p>Your Subtitle Here</p></div>
</section>

<section class="slide">
  <div class="abs" style="left:0;right:0;top:0;height:112px;background:var(--navy)"></div>
  <div class="abs" style="right:22px;top:17px;color:#fff;font-family:Raleway,sans-serif;font-weight:700;font-size:7px;letter-spacing:1.2px">QUARVEX</div>
  <h2 class="abs" style="left:14px;top:42px;color:#fff;font-family:Raleway,sans-serif;font-weight:700;font-size:15px;line-height:1.3">Our Mock<br>Up Area</h2>
  <div class="photo" role="img" aria-label="Laptop mockup showing a Quarvex title screen" style="left:100px;top:30px;width:136px;height:84px;background:linear-gradient(180deg,#2a3a62 0%,#4a5676 70%,#c4c9d2 100%)"></div>
  <div class="feat" style="left:14px;top:128px;width:70px;text-align:right"><b>Your Text Here</b>Lorem ipsum dolor sit amet.</div>
  <div class="icon" style="left:96px;top:130px;width:11px;height:11px;background:var(--navy)"><svg viewBox="0 0 10 10"><circle cx="5" cy="5" r="3" fill="none" stroke="#fff" stroke-width="1.2"/></svg></div>
  <div class="feat" style="left:14px;top:152px;width:70px;text-align:right"><b>Your Text Here</b>Lorem ipsum dolor sit amet.</div>
  <div class="icon" style="left:96px;top:154px;width:11px;height:11px;background:var(--navy)"><svg viewBox="0 0 10 10"><path d="M2 5l2 2 4-4" fill="none" stroke="#fff" stroke-width="1.2"/></svg></div>
  <div class="icon" style="left:234px;top:130px;width:11px;height:11px;background:var(--navy)"><svg viewBox="0 0 10 10"><rect x="2.5" y="2.5" width="5" height="5" fill="#fff"/></svg></div>
  <div class="feat" style="left:250px;top:128px;width:70px"><b>Your Text Here</b>Lorem ipsum dolor sit amet.</div>
  <div class="icon" style="left:234px;top:154px;width:11px;height:11px;background:var(--navy)"><svg viewBox="0 0 10 10"><path d="M5 2v6M2 5h6" stroke="#fff" stroke-width="1.2"/></svg></div>
  <div class="feat" style="left:250px;top:152px;width:70px"><b>Your Text Here</b>Lorem ipsum dolor sit amet.</div>
  <div class="footer"><span>© 2017 QUARVEX. All rights reserved</span><span>43</span></div>
</section>

<section class="slide">
  <h2 class="abs" style="left:14px;top:26px;font-family:Raleway,sans-serif;font-weight:700;font-size:14px;line-height:.95">Video Title<br>Goes Here</h2>
  <div class="badge">QUARVEX</div>
  <p class="abs tiny" style="left:14px;top:72px;width:70px">Lorem ipsum dolor sit amet, consectetur adipiscing elit, sed do eiusmod tempor incididunt ut labore et dolore magna aliqua.</p>
  <p class="abs tiny" style="left:14px;top:104px;width:70px">Duis aute irure dolor in reprehenderit in voluptate velit esse cillum dolore eu fugiat nulla pariatur.</p>
  <p class="abs tiny" style="left:14px;top:134px;width:70px">Ut enim ad minim veniam, quis nostrud exercitation laboris.</p>
  <div class="photo" role="img" aria-label="Desktop monitor mockup playing a video of a person signing documents" style="left:99px;top:28px;width:188px;height:143px;background:linear-gradient(160deg,#e9ecef 0%,#cfd5dc 50%,#9aa3af 100%)"></div>
  <div class="footer"><span>© 2017 QUARVEX. All rights reserved</span><span>44</span></div>
</section>

<section class="slide">
  <h2 class="title">Four Column Area</h2><div class="badge">QUARVEX</div>
  <p class="abs tiny" style="left:27px;top:50px;width:275px">Lorem ipsum dolor sit amet, consectetur adipiscing elit, sed do eiusmod tempor incididunt ut labore et dolore magna aliqua. Ut enim ad minim veniam, quis nostrud exercitation ullamco laboris nisi ut aliquip ex ea commodo consequat.</p>
  <div class="col-box" style="left:25px;background:var(--navy)"><div class="icon"><svg viewBox="0 0 10 10"><circle cx="5" cy="5" r="2.5" fill="var(--navy)"/></svg></div><b>YOUR TEXT HERE</b>Lorem ipsum dolor sit consectetur adipiscing elit.</div>
  <div class="col-box" style="left:96px;background:var(--teal)"><div class="icon"><svg viewBox="0 0 10 10"><path d="M2 7h6L7 3 5 5 3 3z" fill="var(--teal)"/></svg></div><b>YOUR TEXT HERE</b>Lorem ipsum dolor sit consectetur adipiscing elit.</div>
  <div class="col-box" style="left:167px;background:var(--navy)"><div class="icon"><svg viewBox="0 0 10 10"><path d="M2 8l6-6M5 2h3v3" fill="none" stroke="var(--navy)" stroke-width="1.3"/></svg></div><b>YOUR TEXT HERE</b>Lorem ipsum dolor sit consectetur adipiscing elit.</div>
  <div class="col-box" style="left:238px;background:var(--blue)"><div class="icon"><svg viewBox="0 0 10 10"><path d="M3 2h4v2a2 2 0 01-4 0zM5 6v2M3.5 8h3" fill="none" stroke="var(--blue)" stroke-width="1.1"/></svg></div><b>YOUR TEXT HERE</b>Lorem ipsum dolor sit consectetur adipiscing elit.</div>
  <div class="footer"><span>© 2017 QUARVEX. All rights reserved</span><span>45</span></div>
</section>

<section class="slide">
  <h2 class="title">Four Column Area</h2><div class="badge">QUARVEX</div>
  <p class="abs tiny center" style="left:40px;top:41px;width:250px">Lorem ipsum dolor sit amet, consectetur adipiscing elit, sed do eiusmod tempor incididunt ut labore et dolore magna aliqua. Ut enim ad minim veniam, quis nostrud exercitation ullamco laboris nisi ut aliquip commodo consequat.</p>
  <div class="col-item tiny" style="left:36px"><div class="ring" style="border-color:var(--navy)"><svg viewBox="0 0 10 10" width="16" height="16"><path d="M3 2h4v2a2 2 0 01-4 0zM5 6v2M3.5 8h3" fill="none" stroke="var(--navy)" stroke-width="1"/></svg></div><h5>COLUMN 1</h5>Lorem ipsum dolor sit amet, consectetur adipiscing elit, sed do eiusmod tempor incididunt ut labore magna.</div>
  <div class="col-item tiny" style="left:101px"><div class="ring" style="border-color:var(--blue)"><svg viewBox="0 0 10 10" width="16" height="16"><path d="M2 7h6L7 3 5 5 3 3z" fill="var(--blue)"/></svg></div><h5>COLUMN 2</h5>Lorem ipsum dolor sit amet, consectetur adipiscing elit, sed do eiusmod tempor incididunt ut labore magna.</div>
  <div class="col-item tiny" style="left:166px"><div class="ring" style="border-color:var(--teal)"><svg viewBox="0 0 10 10" width="16" height="16"><path d="M2 8l6-6M5 2h3v3" fill="none" stroke="var(--teal)" stroke-width="1.2"/></svg></div><h5>COLUMN 3</h5>Lorem ipsum dolor sit amet, consectetur adipiscing elit, sed do eiusmod tempor incididunt ut labore magna.</div>
  <div class="col-item tiny" style="left:231px"><div class="ring" style="border-color:var(--navy)"><svg viewBox="0 0 10 10" width="16" height="16"><circle cx="5" cy="5" r="2.6" fill="var(--navy)"/></svg></div><h5>COLUMN 4</h5>Lorem ipsum dolor sit amet, consectetur adipiscing elit, sed do eiusmod tempor incididunt ut labore magna.</div>
  <div class="footer"><span>© 2017 QUARVEX. All rights reserved</span><span>46</span></div>
</section>

<section class="slide">
  <h2 class="title">Key Points Area</h2><div class="badge">QUARVEX</div>
  <p class="abs tiny" style="left:20px;top:54px;width:290px">Lorem ipsum dolor sit amet, consectetur adipiscing elit, sed do eiusmod tempor incididunt ut labore et dolore magna aliqua. Ut enim ad minim veniam, quis nostrud exercitation ullamco laboris nisi ut aliquip ex ea commodo consequat.</p>
  <div class="kp" style="left:62px;background:var(--navy)"><svg viewBox="0 0 10 10"><circle cx="3.5" cy="4" r="1.5" fill="#fff"/><circle cx="6.5" cy="4" r="1.5" fill="#fff"/><path d="M1 9a2.5 2.5 0 015 0zM4 9a2.5 2.5 0 015 0z" fill="#fff"/></svg>Lorem<br>ipsum</div>
  <div class="kp" style="left:101px;background:var(--teal)"><svg viewBox="0 0 10 10"><path d="M2 8l5-5 1 1-5 5z" fill="#fff"/></svg>Lorem<br>ipsum</div>
  <div class="kp" style="left:140px;background:var(--blue)"><svg viewBox="0 0 10 10"><path d="M2 6h1.5v3H2zM4.3 4h1.5v5H4.3zM6.6 2h1.5v7H6.6z" fill="#fff"/></svg>Lorem<br>ipsum</div>
  <div class="kp" style="left:179px;background:var(--teal-light)"><svg viewBox="0 0 10 10"><path d="M5 8.5L1.5 5a2 2 0 013.5-2.5A2 2 0 018.5 5z" fill="#fff"/></svg>Lorem<br>ipsum</div>
  <div class="kp" style="left:218px;background:var(--navy)"><svg viewBox="0 0 10 10"><path d="M2 7h6L7 3 5 5 3 3z" fill="#fff"/></svg>Lorem<br>ipsum</div>
  <p class="abs tiny center" style="left:55px;top:134px;width:220px">Lorem ipsum dolor sit amet, consectetur adipiscing elit, sed do eiusmod tempor incididunt ut labore et dolore magna aliqua. Ut enim ad minim veniam, quis nostrud exercitation ullamco laboris nisi ut aliquip commodo.</p>
  <div class="footer"><span>© 2017 QUARVEX. All rights reserved</span><span>47</span></div>
</section>

<section class="slide">
  <h2 class="title">Workflow Area</h2><div class="badge">QUARVEX</div>
  <p class="abs tiny" style="left:24px;top:50px;width:285px">Lorem ipsum dolor sit amet, consectetur adipiscing elit, sed do eiusmod tempor incididunt ut labore et dolore magna aliqua. Ut enim ad minim veniam, quis nostrud exercitation ullamco laboris nisi ut aliquip ex ea commodo consequat.</p>
  <svg class="abs" style="left:0;top:0" width="325" height="183" viewBox="0 0 325 183">
    <g fill="none" stroke-width="8">
      <path d="M30 112 A27 27 0 0 1 84 112" stroke="#1d2a4e"/>
      <path d="M84 112 A27 27 0 0 0 138 112" stroke="#0792cd"/>
      <path d="M138 112 A27 27 0 0 1 192 112" stroke="#1d2a4e"/>
      <path d="M192 112 A27 27 0 0 0 246 112" stroke="#0792cd"/>
      <path d="M246 112 A27 27 0 0 1 300 112" stroke="#1d2a4e"/>
    </g>
    <g font-family="Open Sans" font-size="3.5" text-anchor="middle">
      <circle cx="57" cy="97" r="4" fill="#1d2a4e"/><text x="57" y="98.3" fill="#fff">1</text>
      <circle cx="111" cy="127" r="4" fill="#0792cd"/><text x="111" y="128.3" fill="#fff">2</text>
      <circle cx="165" cy="97" r="4" fill="#1d2a4e"/><text x="165" y="98.3" fill="#fff">3</text>
      <circle cx="219" cy="127" r="4" fill="#0792cd"/><text x="219" y="128.3" fill="#fff">4</text>
      <circle cx="273" cy="97" r="4" fill="#1d2a4e"/><text x="273" y="98.3" fill="#fff">5</text>
    </g>
  </svg>
  <div class="feat center" style="left:40px;top:107px;width:34px"><b>Data 1</b>Lorem ipsum dolor sit amet consectetur.</div>
  <div class="feat center" style="left:92px;top:75px;width:38px"><b style="color:var(--blue)">Data 2</b>Lorem ipsum dolor sit amet consectetur.</div>
  <div class="feat center" style="left:148px;top:107px;width:34px"><b>Data 3</b>Lorem ipsum dolor sit amet consectetur.</div>
  <div class="feat center" style="left:200px;top:75px;width:38px"><b style="color:var(--blue)">Data 4</b>Lorem ipsum dolor sit amet consectetur.</div>
  <div class="feat center" style="left:256px;top:107px;width:34px"><b>Data 5</b>Lorem ipsum dolor sit amet consectetur.</div>
  <div class="footer"><span>© 2017 QUARVEX. All rights reserved</span><span>48</span></div>
</section>

<section class="slide">
  <h2 class="title">Timeline</h2><div class="badge">QUARVEX</div>
  <svg class="abs" style="left:0;top:0" width="325" height="183"><g stroke="#b8bec9" stroke-width=".7"><line x1="44" y1="87" x2="280" y2="87"/><line x1="84" y1="72" x2="84" y2="87"/><line x1="162" y1="72" x2="162" y2="87"/><line x1="240" y1="72" x2="240" y2="87"/><line x1="123" y1="87" x2="123" y2="104"/><line x1="201" y1="87" x2="201" y2="104"/></g></svg>
  <div class="year" style="left:27px;top:78px;background:var(--navy)">2010<small>Your Text<br>Goes Here</small></div>
  <div class="year" style="left:66px;top:40px;background:var(--blue)">2011<small>Your Text<br>Goes Here</small></div>
  <div class="year" style="left:105px;top:104px;background:var(--teal)">2012<small>Your Text<br>Goes Here</small></div>
  <div class="year" style="left:144px;top:40px;background:var(--teal-light)">2013<small>Your Text<br>Goes Here</small></div>
  <div class="year" style="left:183px;top:104px;background:var(--teal)">2014<small>Your Text<br>Goes Here</small></div>
  <div class="year" style="left:222px;top:40px;background:var(--blue)">2015<small>Your Text<br>Goes Here</small></div>
  <div class="year" style="left:262px;top:69px;background:var(--navy);border:2px solid #fff;box-shadow:0 0 0 1px var(--navy)">2018<small>Your Text<br>Goes Here</small></div>
  <div class="feat" style="left:230px;top:114px;width:82px;text-align:right"><b style="font-weight:400">Your Text Goes Here</b>Lorem ipsum dolor sit amet, consectetur adipiscing elit, sed do eiusmod tempor incididunt labore.</div>
  <div class="feat" style="left:14px;top:150px;width:140px"><b style="font-weight:400">Your Text Goes Here</b>Lorem ipsum dolor sit amet, consectetur adipiscing elit, sed do eiusmod tempor incididunt labore magna.</div>
  <div class="footer"><span>© 2017 QUARVEX. All rights reserved</span><span>49</span></div>
</section>

<section class="slide">
  <h2 class="title">Our Team</h2><div class="badge">QUARVEX</div>
  <div class="member" style="left:20px;top:47px"><div class="avatar" role="img" aria-label="Portrait photo of Michael Doe" style="background:linear-gradient(160deg,#c9ced6,#8b94a3)"></div><div class="member-info"><h5>Michael Doe</h5><p>CEO<br>MSc, MBA and CFA Dip PM</p><ul><li>Lorem ipsum dolor sit amet, consectetur adipiscing elit</li><li>Sed do eiusmod tempor incididunt ut labore</li><li>Ut enim ad minim veniam, quis nostrud</li></ul></div></div>
  <div class="member" style="left:170px;top:47px"><div class="avatar" role="img" aria-label="Portrait photo of James Doe" style="background:linear-gradient(160deg,#e4e7ec,#a7aeba)"></div><div class="member-info"><h5>James Doe</h5><p>MANAGER<br>M.B.A</p><ul><li>Lorem ipsum dolor sit amet, consectetur adipiscing elit</li><li>Sed do eiusmod tempor incididunt ut labore</li><li>Ut enim ad minim veniam, quis nostrud</li></ul></div></div>
  <div class="member" style="left:20px;top:109px"><div class="avatar" role="img" aria-label="Portrait photo of Jane Doe" style="background:linear-gradient(160deg,#ecd9c6,#b39b86)"></div><div class="member-info"><h5>Jane Doe</h5><p>Doctor of Chemistry<br>M.B.A</p><ul><li>Lorem ipsum dolor sit amet, consectetur adipiscing elit</li><li>Sed do eiusmod tempor incididunt ut labore</li><li>Ut enim ad minim veniam, quis nostrud</li></ul></div></div>
  <div class="member" style="left:170px;top:109px"><div class="avatar" role="img" aria-label="Portrait photo of John Doe" style="background:linear-gradient(160deg,#d8dde4,#7d8796)"></div><div class="member-info"><h5>John Doe</h5><p>Doctor of Physical<br>Professor</p><ul><li>Lorem ipsum dolor sit amet, consectetur adipiscing elit</li><li>Sed do eiusmod tempor incididunt ut labore</li><li>Ut enim ad minim veniam, quis nostrud</li></ul></div></div>
  <div class="footer"><span>© 2017 QUARVEX. All rights reserved</span><span>50</span></div>
</section>

<section class="slide">
  <h2 class="title">Customer Testimonials</h2><div class="badge">QUARVEX</div>
  <div class="abs" style="left:0;right:0;top:99px;bottom:0;background:var(--navy)"></div>
  <div class="abs" style="left:107px;top:95px;width:10px;height:10px;background:var(--navy);transform:rotate(45deg)"></div>
  <div class="avatar" role="img" aria-label="Portrait photo of a client" style="left:87px;top:42px;width:44px;height:44px;background:linear-gradient(160deg,#d8dde4,#7d8796);border:2px solid #fff;box-shadow:0 0 0 .5px #ccc"></div>
  <p class="abs tiny" style="left:140px;top:54px;width:160px">Adipiscing elit, sed diam nonummy nibh euismod tincidunt ut laoreet dolore magna aliquam erat volutpat. Ut wisi enim <b>Lorem ipsum</b> dolor sit amet, consectetur adipiscing elit, sed diam nonummy nibh euismod tincidunt ut laoreet dolore magna.</p>
  <div class="icon" style="left:68px;top:113px;width:22px;height:22px;border:1px solid #fff"><svg viewBox="0 0 10 10"><rect x="2" y="2.5" width="6" height="5" fill="none" stroke="#fff" stroke-width=".8"/></svg></div>
  <div class="icon" style="left:129px;top:113px;width:22px;height:22px;border:1px solid #fff"><svg viewBox="0 0 10 10"><path d="M2 3h6v5H2zM2 3l3 2 3-2" fill="none" stroke="#fff" stroke-width=".8"/></svg></div>
  <div class="icon" style="left:191px;top:113px;width:22px;height:22px;border:1px solid #fff"><svg viewBox="0 0 10 10"><path d="M2 2h6v6H2zM4 4h2v2H4z" fill="none" stroke="#fff" stroke-width=".8"/></svg></div>
  <div class="icon" style="left:253px;top:113px;width:22px;height:22px;border:1px solid #fff"><svg viewBox="0 0 10 10"><path d="M2 3h6v4H2zM4 3v4M6 3v4" fill="none" stroke="#fff" stroke-width=".8"/></svg></div>
  <p class="abs tiny center" style="left:56px;top:141px;width:46px;color:#c9cfdc;font-size:3.4px">Why does getting a loan have to be so much more complicated than ordering a fridge online?</p>
  <p class="abs tiny center" style="left:117px;top:141px;width:46px;color:#c9cfdc;font-size:3.4px">Why do I have to go to a branch, fill out forms and wait for weeks to get a response?</p>
  <p class="abs tiny center" style="left:179px;top:141px;width:46px;color:#c9cfdc;font-size:3.4px">Why do banks refuse to lend to me despite the substantial fees I receive each month?</p>
  <p class="abs tiny center" style="left:241px;top:141px;width:46px;color:#c9cfdc;font-size:3.4px">Why is there no Northwind in banking, that identifies my needs and offers convenience at fair prices?</p>
</section>

<section class="slide">
  <h2 class="title">Bullet &amp; Chart Area</h2><div class="badge">QUARVEX</div>
  <svg class="abs" style="left:0;top:0" width="325" height="183">
    <g font-family="Open Sans" font-size="3" fill="#9aa0ad">
      <text x="30" y="64">Category 4</text><text x="30" y="88">Category 3</text><text x="30" y="112">Category 2</text><text x="30" y="136">Category 1</text>
    </g>
    <line x1="48" y1="52" x2="48" y2="146" stroke="#dfe3ea" stroke-width=".5"/>
    <rect x="50" y="56" width="88" height="3.5" fill="#0792cd"/><rect x="50" y="60" width="50" height="3.5" fill="#8e929b"/><rect x="50" y="64" width="80" height="3.5" fill="#1d2a4e"/>
    <rect x="50" y="80" width="20" height="3.5" fill="#0792cd"/><rect x="50" y="84" width="52" height="3.5" fill="#8e929b"/><rect x="50" y="88" width="62" height="3.5" fill="#1d2a4e"/>
    <rect x="50" y="104" width="14" height="3.5" fill="#8e929b"/><rect x="50" y="108" width="78" height="3.5" fill="#86cfc6"/><rect x="50" y="112" width="58" height="3.5" fill="#1d2a4e"/>
    <rect x="50" y="128" width="14" height="3.5" fill="#0792cd"/><rect x="50" y="132" width="40" height="3.5" fill="#8e929b"/><rect x="50" y="136" width="100" height="3.5" fill="#1d2a4e"/>
  </svg>
  <div class="legend" style="left:68px;top:151px"><span><i style="background:#1d2a4e"></i>Series 3</span><span><i style="background:#8e929b"></i>Series 2</span><span><i style="background:#0792cd"></i>Series 1</span></div>
  <div class="icon" style="left:180px;top:57px;width:11px;height:11px;background:var(--navy)"><svg viewBox="0 0 10 10"><circle cx="4.5" cy="4.5" r="2" fill="none" stroke="#fff" stroke-width="1"/><path d="M6 6l2 2" stroke="#fff" stroke-width="1"/></svg></div>
  <div class="feat" style="left:199px;top:56px;width:100px"><b style="font-weight:400">Category One</b>Lorem ipsum dolor sit amet, consectetur adipiscing elit, sed do eiusmod.</div>
  <div class="icon" style="left:180px;top:83px;width:11px;height:11px;background:var(--navy)"><svg viewBox="0 0 10 10"><circle cx="4.5" cy="4.5" r="2" fill="none" stroke="#fff" stroke-width="1"/><path d="M6 6l2 2" stroke="#fff" stroke-width="1"/></svg></div>
  <div class="feat" style="left:199px;top:82px;width:100px"><b style="font-weight:400">Category Two</b>Lorem ipsum dolor sit amet, consectetur adipiscing elit, sed do eiusmod.</div>
  <div class="icon" style="left:180px;top:109px;width:11px;height:11px;background:var(--navy)"><svg viewBox="0 0 10 10"><path d="M2 8l6-6M5 2h3v3" fill="none" stroke="#fff" stroke-width="1"/></svg></div>
  <div class="feat" style="left:199px;top:108px;width:100px"><b style="font-weight:400">Category Three</b>Lorem ipsum dolor sit amet, consectetur adipiscing elit, sed do eiusmod.</div>
  <div class="icon" style="left:180px;top:135px;width:11px;height:11px;background:var(--navy)"><svg viewBox="0 0 10 10"><circle cx="5" cy="5" r="2.2" fill="none" stroke="#fff" stroke-width="1.2"/></svg></div>
  <div class="feat" style="left:199px;top:134px;width:100px"><b style="font-weight:400">Category Four</b>Lorem ipsum dolor sit amet, consectetur adipiscing elit, sed do eiusmod.</div>
  <div class="footer"><span>© 2017 QUARVEX. All rights reserved</span><span>52</span></div>
</section>

<section class="slide">
  <h2 class="title">Bullet &amp; Chart Area</h2><div class="badge">QUARVEX</div>
  <div class="icon" style="left:33px;top:56px;width:11px;height:11px;background:var(--navy)"><svg viewBox="0 0 10 10"><circle cx="4.5" cy="4.5" r="2" fill="none" stroke="#fff" stroke-width="1"/><path d="M6 6l2 2" stroke="#fff" stroke-width="1"/></svg></div>
  <div class="feat" style="left:52px;top:55px;width:100px"><b style="font-weight:400">Your Text Here</b>Lorem ipsum dolor sit amet, consectetur adipiscing elit, sed do eiusmod.</div>
  <div class="icon" style="left:33px;top:83px;width:11px;height:11px;background:var(--teal)"><svg viewBox="0 0 10 10"><path d="M2 8l5-5 1 1-5 5z" fill="#fff"/></svg></div>
  <div class="feat" style="left:52px;top:82px;width:100px"><b style="font-weight:400;color:var(--teal)">Your Text Here</b>Lorem ipsum dolor sit amet, consectetur adipiscing elit, sed do eiusmod.</div>
  <div class="icon" style="left:33px;top:109px;width:11px;height:11px;background:var(--blue)"><svg viewBox="0 0 10 10"><path d="M2 8l6-6M5 2h3v3" fill="none" stroke="#fff" stroke-width="1"/></svg></div>
  <div class="feat" style="left:52px;top:108px;width:100px"><b style="font-weight:400;color:var(--blue)">Your Text Here</b>Lorem ipsum dolor sit amet, consectetur adipiscing elit, sed do eiusmod.</div>
  <div class="icon" style="left:33px;top:135px;width:11px;height:11px;background:var(--teal-light)"><svg viewBox="0 0 10 10"><circle cx="5" cy="5" r="2.2" fill="none" stroke="#fff" stroke-width="1.2"/></svg></div>
  <div class="feat" style="left:52px;top:134px;width:100px"><b style="font-weight:400;color:var(--teal-light)">Your Text Here</b>Lorem ipsum dolor sit amet, consectetur adipiscing elit, sed do eiusmod.</div>
  <svg class="abs" style="left:0;top:0" width="325" height="183">
    <g transform="rotate(-90 235 101)" fill="none" stroke-width="11">
      <circle cx="235" cy="101" r="34" stroke="#1d2a4e" stroke-dasharray="128.2 213.6" stroke-dashoffset="-85.4"/>
      <circle cx="235" cy="101" r="34" stroke="#86cfc6" stroke-dasharray="21.4 213.6" stroke-dashoffset="0"/>
      <circle cx="235" cy="101" r="34" stroke="#33a6d7" stroke-dasharray="32 213.6" stroke-dashoffset="-21.4"/>
      <circle cx="235" cy="101" r="34" stroke="#0792cd" stroke-dasharray="32 213.6" stroke-dashoffset="-53.4"/>
    </g>
    <g fill="#8e929b"><rect x="224" y="104" width="3" height="6"/><rect x="229" y="100" width="3" height="10"/><rect x="234" y="95" width="3" height="15"/><rect x="239" y="91" width="3" height="19"/><rect x="221" y="110" width="24" height=".8"/></g>
    <g font-family="Raleway" font-size="9">
      <text x="220" y="55" fill="#86cfc6">10%</text>
      <text x="182" y="85" fill="#0792cd">15%</text>
      <text x="183" y="124" fill="#8e929b">25%</text>
      <text x="277" y="105" fill="#1d2a4e">60%</text>
    </g>
  </svg>
  <div class="legend" style="left:198px;top:147px"><span><i style="background:#1d2a4e;border-radius:50%"></i>1st Qtr</span><span><i style="background:#33a6d7;border-radius:50%"></i>2nd Qtr</span><span><i style="background:#0792cd;border-radius:50%"></i>3rd Qtr</span><span><i style="background:#86cfc6;border-radius:50%"></i>4th Qtr</span></div>
  <div class="footer"><span>© 2017 QUARVEX. All rights reserved</span><span>53</span></div>
</section>

<section class="slide" style="background:var(--navy)">
  <div class="photo" role="img" aria-label="Tinted photo of a businessman standing at an office window" style="inset:0;background:linear-gradient(120deg,#2b3b63 0%,#3f5079 55%,#2a3a62 100%)"></div>
  <div class="contact-panel">
    <div class="brand">QUARVEX</div>
    <h3>Our Contact</h3>
    <div class="contact-line"><svg viewBox="0 0 10 10"><path d="M1 5l4-4 4 4v4H1z" fill="#fff"/></svg><span>123 Street Road<br>City 12345</span></div>
    <div class="contact-line"><svg viewBox="0 0 10 10"><path d="M2 1h2l1 2-1 1a6 6 0 003 3l1-1 2 1v2h-2A8 8 0 011 2z" fill="#fff"/></svg><span>(123) 456-7890</span></div>
    <div class="contact-line"><svg viewBox="0 0 10 10"><path d="M1 2h8v6H1zM1 2l4 3 4-3" fill="none" stroke="#fff" stroke-width="1"/></svg><span>emailaddress@email.com</span></div>
    <div class="contact-line"><svg viewBox="0 0 10 10"><circle cx="5" cy="5" r="4" fill="#fff"/></svg><span>www.website-address.com</span></div>
    <div class="socials"><span></span><span></span><span></span></div>
  </div>
  <div class="thanks"><h2>THANK YOU</h2><p>For Your Precious Time</p><small>Stop by our office or give us a call!<br>We would love to hear from you.</small></div>
</section>

</main>
</body>
</html>
```